【サイト概要】
可愛くリノベーションした物件を紹介し、入居者を募集する賃貸物件紹介サイトです。
物件紹介だけではなく、周辺の町情報(カフェや雑貨店など)や、暮らしに役立つ情報(収納術や簡単レシピなど)も共に発信し、
物件探しだけでなく女性の暮らしを不動産屋の視点からサポート・応援をするサイトとなります。

【ターゲット】
・主に女性
・部屋探しをしている方
・20代~40代の可愛いものが好きな方
・日々の暮らしがより可愛くなるよう役立つ情報を集めている方

【重視する点】
・可愛らしいデザインが得意な方
・WEBデザインのトンマナに理解のある方
・アイコンや枠・線などの装飾はSVG形式で配置可能なもの(原則単色であり色を変更しても見劣りしないもの)
・PhotoshopまたはXDでデザイン可能な方

【参考サイト】
可愛いの範囲が曖昧になってしまうため、
幾つか参考サイトをピックアップしました。
すべてを兼ね備えたものではなく、
制作者様のお得意なジャンルの“可愛い”に絞っていただきデザインいただければと思います。

▼ナチュラル(北欧風)
https://tenori-kobako.jp/
https://www.mimosoire.jp/
https://www2.torvasu.co.jp/healthcare/pickup/zadankai/
https://www.plum-kitchen.com/

▼ポップ
https://www.sorao.ac.jp/girls/
https://www.mofurin-dots.com/
https://www.harvolin.jp/concert/
https://kumorine-hiraso.or.jp/

▼エレガント
http://tipsvelo.com/
http://rozu-bridal.jp/
https://lumiroe.jp/

【素材について】
Googleドライブに格納しております。
https://files.kamitoru.jp/drive/folders/8KpeRtzXa4LmNoQvBc2YhWsUdFjGiEHxL?usp=sharing
・写真
・イラスト
・見出しの英語サブタイトルなどにはGoogle Fontsから使用可
・アイコンには、Awesomeフォント(Free)やGoogle iconも使用可

※ドライブに格納している素材写真ですが物件や記事の写真にお使いください。
その他必要な写真素材がありましたら、一旦フリー素材や有料レンポジサイトのウォーターマーク入りの仮素材にて作成ください。最終差し替え作業は当方にて行うため不要です。
※イラスト素材についてはこちらで用意できたものを格納しておりますが、使用の有無はお任せいたします。

【デザイン作成に際しご留意いただきたい点】
フォント及びフォントサイズについてはワイヤーのものは参考とせず、作成いただくデザインに準じたフォント及びサイズの選定・規定をお願いいたします。
Googleフォントの使用を想定していますので、システムフォントを使用する箇所についてのフォント選定の参考としてください。

【トンマナのルール化】
WordPressにて実装いたしますので、色味や要素の大きさなど、デザインから色や形の使用ルールが見えるデザインをお願いしたいです。

その他何かご不明な点がございましたら、お気軽にご質問下さい。
よろしくお願いいたします。
赤系、黄・オレンジ系、茶系、線やアイコンの色を変えても使用可能なデザインを希望しています
XDデータでも可
期間が短かったため、ゆとりを持ってご提案いただけるように締め切りを延長いたしました。
少しでもご興味を持っていただけましたら、是非ご応募ください。
良いご縁がありますことを願っております。
とても良いご提案を数件頂いておりますので、
さらに期間を延長させていただいて検討したいと思います。

・社員全員とも相談をし多数決で決定いたしました
・ベース色を変えたときにも利用しやすそうだった

多くの皆様からかわいいご提案を頂きまして、本当にありがとうございました。
すべての方をご当選できればよいのですが、1名となってしまいますこと何卒ご了承ください。
ご提案頂きました9名の皆様には、改めましてお礼申し上げます。
本当にありがとうございました。

```html
<!DOCTYPE html>
<html lang="ja">
<head>
<meta charset="utf-8">
<title>ふわりのおへや｜可愛い賃貸物件紹介</title>
<link href="https://fonts.googleapis.com/css2?family=Noto+Sans+JP:wght@400;500;700&family=Kaushan+Script&display=swap" rel="stylesheet">
<style>
:root{
  --pink:#f19db1;
  --pink-deep:#e9788f;
  --pink-pale:#fdeef2;
  --pink-line:#f6c9d4;
  --text:#3a3a3a;
  --sub:#888;
  --white:#fff;
  --green:#3fb868;
  --dark:#3a3a3a;
  --photo-room:linear-gradient(135deg,#e9e5e2,#c9c4c2);
  --photo-building:linear-gradient(180deg,#cfdceb,#b6b1b4 60%,#8f8a8d);
  --photo-food:linear-gradient(135deg,#c9a27a,#6e5644);
  --photo-person:linear-gradient(135deg,#f6e5e3,#d7b9b6);
}
*{box-sizing:border-box;margin:0;padding:0}
html,body{width:1200px;height:3096px;overflow:hidden}
body{font-family:"Noto Sans JP",sans-serif;color:var(--text);background:var(--white);position:relative;font-size:13px}
.abs{position:absolute}
.ph{display:block;border-radius:4px}
.ph.room{background:var(--photo-room)}
.ph.bld{background:var(--photo-building)}
.ph.food{background:var(--photo-food)}
.ph.person{background:var(--photo-person)}

/* top bar */
.topbar{left:0;top:0;width:1200px;height:32px;background:var(--pink);color:var(--white);font-size:11px;display:flex;align-items:center;justify-content:space-between;padding:0 20px}
.topbar ul{display:flex;list-style:none;gap:4px}
.topbar li{background:var(--white);color:var(--pink-deep);padding:3px 12px;font-size:11px}
.gnav{left:0;top:32px;width:1200px;height:44px;display:flex;list-style:none;padding-left:20px;gap:6px;align-items:center}
.gnav li{border:1px solid var(--pink-line);padding:6px 18px;font-size:12px}
.logo{left:0;top:96px;width:1200px;text-align:center;display:flex;justify-content:center;align-items:center;gap:10px}
.logo .name{font-size:40px;font-weight:700;color:var(--pink)}
.logo .mark{width:30px;height:30px;border-radius:50%;background:var(--pink)}

/* slider */
.slider{left:-110px;top:200px;display:flex;gap:24px}
.slide{width:350px}
.slide .ph{height:250px;position:relative}
.tag{position:absolute;left:10px;bottom:10px;background:var(--white);color:var(--pink-deep);font-size:11px;padding:2px 10px;border-radius:10px}
.slide p{font-size:15px;line-height:1.5;margin-top:8px;font-weight:500}

/* headings */
.hd{text-align:center}
.hd .en{font-family:"Kaushan Script",cursive;font-size:44px;line-height:1}
.hd .ja{display:block;font-size:10px;color:var(--pink-deep);margin-top:2px}
.hd-new{left:0;top:536px;width:1200px}

/* property grid */
.props{left:90px;top:620px;width:1020px;display:grid;grid-template-columns:repeat(4,1fr);gap:24px 16px}
.prop{font-size:11px;line-height:1.5}
.prop .ph{height:150px;position:relative}
.badge{position:absolute;left:0;top:0;background:var(--pink);color:var(--white);font-size:10px;padding:3px 8px}
.price{font-size:22px;color:var(--pink-deep);font-weight:700;line-height:1.2;margin-top:6px;display:flex;align-items:baseline;justify-content:space-between}
.price small{font-size:10px;color:var(--sub);font-weight:400}
.prop h3{font-size:12px;font-weight:500;margin:4px 0}
.prop .meta{color:var(--sub);display:flex;justify-content:space-between}
.heart{width:14px;height:14px}

/* columns */
.hd-col{left:100px;top:1450px;width:640px}
.hd-rank{left:800px;top:1450px;width:300px}
.cols{left:100px;top:1540px;width:640px;display:grid;grid-template-columns:1fr 1fr;gap:26px 20px}
.col .ph{height:196px;position:relative}
.col p{font-size:14px;font-weight:500;line-height:1.5;margin-top:6px}
.pager{left:100px;top:2450px;width:640px;display:flex;justify-content:center;gap:6px;list-style:none}
.pager li{width:26px;height:26px;border:1px solid var(--pink-line);font-size:11px;display:flex;align-items:center;justify-content:center}
.pager li.on{background:var(--pink);color:var(--white);border-color:var(--pink)}

/* ranking */
.rank{left:800px;top:1540px;width:300px;list-style:none}
.rank li{display:flex;gap:10px;padding:8px 0;border-bottom:1px solid var(--pink-line);font-size:11px;line-height:1.5}
.rank .ph{width:90px;height:60px;flex:none;border-radius:2px}
.rank b{display:block;font-weight:500}
.rank .pr{color:var(--pink-deep);font-weight:700}
.hd-other{left:800px;top:2240px;width:300px}
.other{left:800px;top:2320px;width:300px;list-style:none}
.other li{display:flex;align-items:center;justify-content:space-between;border:1px solid var(--pink-line);margin-bottom:10px;height:56px;padding-left:14px;font-size:13px;background:var(--pink-pale)}
.other .ph{width:120px;height:54px;border-radius:0}

/* contact */
.contact{left:100px;top:2664px;width:1000px;height:170px;border:1px solid var(--pink-line);border-radius:8px;text-align:center;padding-top:22px}
.contact p{font-size:12px}
.contact .row{display:flex;align-items:center;justify-content:center;gap:30px;margin-top:34px}
.tel{display:flex;align-items:center;gap:8px;font-size:30px;font-weight:700;color:var(--pink-deep)}
.tel small{display:block;font-size:10px;color:var(--sub);font-weight:400}
.btn{width:200px;height:46px;display:flex;align-items:center;justify-content:center;color:var(--white);font-size:13px;border-radius:3px}
.btn.talk{background:var(--green)}
.btn.mail{background:var(--dark)}

/* footer */
.footer{left:0;top:2880px;width:1200px;height:216px;background:var(--pink-pale)}
.f-logo{left:120px;top:34px;display:flex;align-items:center;gap:8px}
.f-logo .name{font-size:24px;font-weight:700;color:var(--pink)}
.f-logo .mark{width:20px;height:20px;border-radius:50%;background:var(--pink)}
.f-co{left:120px;top:80px;font-size:12px;line-height:1.6}
.f-co b{font-size:14px}
.f-links{left:400px;top:40px;list-style:none;font-size:11px;line-height:1.9}
.f-sns{left:800px;top:40px;list-style:none;font-size:11px;line-height:1.9}
.copy{left:0;top:186px;width:1200px;height:30px;background:var(--pink);color:var(--white);font-size:10px;text-align:center;line-height:30px}
</style>
</head>
<body>

<header>
  <div class="abs topbar">
    <span>あなたの暮らしにもっと可愛いを。女性の暮らしを応援する不動産サイト</span>
    <ul><li>よくある質問</li><li>お問い合わせ</li><li>会員ログイン</li></ul>
  </div>
  <ul class="abs gnav">
    <li>ライフからさがす</li><li>エリアからさがす</li><li>間取りからさがす</li><li>家賃からさがす</li>
  </ul>
  <div class="abs logo"><span class="name">ふわりのおへや</span><span class="mark"></span></div>
</header>

<section class="abs slider">
  <article class="slide"><div class="ph food" role="img" aria-label="作り置きおかずの写真"><span class="tag">簡単レシピ</span></div><p>ひとり暮らしの簡単すぎる作り置き7日分材料費900円で料理してみた</p></article>
  <article class="slide"><div class="ph person" role="img" aria-label="部屋でくつろぐ女性の写真"><span class="tag">暮らし</span></div><p>ひとり暮らしに必要なものってなに？買ってよかったもの、後悔したもの。</p></article>
  <article class="slide"><div class="ph room" role="img" aria-label="白いワンルームの部屋の写真"><span class="tag">お部屋紹介</span></div><p>はじまりは独身時から。自分を発揮した一人暮らしのワンルームインテリアを拝見</p></article>
  <article class="slide"><div class="ph food" role="img" aria-label="朝ごはんの写真"><span class="tag">簡単レシピ</span></div><p>ひとり暮らしの簡単すぎる作り置き7日分材料費900円で料理してみた</p></article>
</section>

<div class="abs hd hd-new"><span class="en">NEW</span><span class="ja">新着物件</span></div>

<section class="abs props">
  <!-- 12 property cards -->
  <article class="prop"><div class="ph bld" role="img" aria-label="マンション外観の写真"><span class="badge">NEW</span></div><div class="price">7.8万<small>管理費5,000円</small></div><h3>三重中央コロトク・ロフト付き高級物件 パラダン</h3><div class="meta"><span>1K / 24.5㎡ / 駅徒歩5分</span><svg class="heart" viewBox="0 0 24 24"><path d="M12 21s-8-5.2-8-11a4.5 4.5 0 0 1 8-2.8A4.5 4.5 0 0 1 20 10c0 5.8-8 11-8 11z" fill="none" stroke="#e9788f" stroke-width="2"/></svg></div></article>
  <article class="prop"><div class="ph bld" role="img" aria-label="マンション外観の写真"><span class="badge">NEW</span></div><div class="price">7.8万<small>管理費5,000円</small></div><h3>三重中央コロトク・ロフト付き高級物件 パラダン</h3><div class="meta"><span>1K / 24.5㎡ / 駅徒歩5分</span><svg class="heart" viewBox="0 0 24 24"><path d="M12 21s-8-5.2-8-11a4.5 4.5 0 0 1 8-2.8A4.5 4.5 0 0 1 20 10c0 5.8-8 11-8 11z" fill="none" stroke="#e9788f" stroke-width="2"/></svg></div></article>
  <article class="prop"><div class="ph bld" role="img" aria-label="マンション外観の写真"><span class="badge">NEW</span></div><div class="price">7.8万<small>管理費5,000円</small></div><h3>三重中央コロトク・ロフト付き高級物件 パラダン</h3><div class="meta"><span>1K / 24.5㎡ / 駅徒歩5分</span><svg class="heart" viewBox="0 0 24 24"><path d="M12 21s-8-5.2-8-11a4.5 4.5 0 0 1 8-2.8A4.5 4.5 0 0 1 20 10c0 5.8-8 11-8 11z" fill="none" stroke="#e9788f" stroke-width="2"/></svg></div></article>
  <article class="prop"><div class="ph bld" role="img" aria-label="マンション外観の写真"><span class="badge">NEW</span></div><div class="price">7.8万<small>管理費5,000円</small></div><h3>三重中央コロトク・ロフト付き高級物件 パラダン</h3><div class="meta"><span>1K / 24.5㎡ / 駅徒歩5分</span><svg class="heart" viewBox="0 0 24 24"><path d="M12 21s-8-5.2-8-11a4.5 4.5 0 0 1 8-2.8A4.5 4.5 0 0 1 20 10c0 5.8-8 11-8 11z" fill="none" stroke="#e9788f" stroke-width="2"/></svg></div></article>
  <article class="prop"><div class="ph bld" role="img" aria-label="マンション外観の写真"><span class="badge">NEW</span></div><div class="price">7.8万<small>管理費5,000円</small></div><h3>三重中央コロトク・ロフト付き高級物件 パラダン</h3><div class="meta"><span>1K / 24.5㎡ / 駅徒歩5分</span><svg class="heart" viewBox="0 0 24 24"><path d="M12 21s-8-5.2-8-11a4.5 4.5 0 0 1 8-2.8A4.5 4.5 0 0 1 20 10c0 5.8-8 11-8 11z" fill="#e9788f"/></svg></div></article>
  <article class="prop"><div class="ph bld" role="img" aria-label="マンション外観の写真"><span class="badge">NEW</span></div><div class="price">7.8万<small>管理費5,000円</small></div><h3>三重中央コロトク・ロフト付き高級物件 パラダン</h3><div class="meta"><span>1K / 24.5㎡ / 駅徒歩5分</span><svg class="heart" viewBox="0 0 24 24"><path d="M12 21s-8-5.2-8-11a4.5 4.5 0 0 1 8-2.8A4.5 4.5 0 0 1 20 10c0 5.8-8 11-8 11z" fill="none" stroke="#e9788f" stroke-width="2"/></svg></div></article>
  <article class="prop"><div class="ph bld" role="img" aria-label="マンション外観の写真"><span class="badge">NEW</span></div><div class="price">7.8万<small>管理費5,000円</small></div><h3>三重中央コロトク・ロフト付き高級物件 パラダン</h3><div class="meta"><span>1K / 24.5㎡ / 駅徒歩5分</span><svg class="heart" viewBox="0 0 24 24"><path d="M12 21s-8-5.2-8-11a4.5 4.5 0 0 1 8-2.8A4.5 4.5 0 0 1 20 10c0 5.8-8 11-8 11z" fill="none" stroke="#e9788f" stroke-width="2"/></svg></div></article>
  <article class="prop"><div class="ph bld" role="img" aria-label="マンション外観の写真"><span class="badge">NEW</span></div><div class="price">7.8万<small>管理費5,000円</small></div><h3>三重中央コロトク・ロフト付き高級物件 パラダン</h3><div class="meta"><span>1K / 24.5㎡ / 駅徒歩5分</span><svg class="heart" viewBox="0 0 24 24"><path d="M12 21s-8-5.2-8-11a4.5 4.5 0 0 1 8-2.8A4.5 4.5 0 0 1 20 10c0 5.8-8 11-8 11z" fill="none" stroke="#e9788f" stroke-width="2"/></svg></div></article>
  <article class="prop"><div class="ph bld" role="img" aria-label="マンション外観の写真"><span class="badge">NEW</span></div><div class="price">7.8万<small>管理費5,000円</small></div><h3>三重中央コロトク・ロフト付き高級物件 パラダン</h3><div class="meta"><span>1K / 24.5㎡ / 駅徒歩5分</span><svg class="heart" viewBox="0 0 24 24"><path d="M12 21s-8-5.2-8-11a4.5 4.5 0 0 1 8-2.8A4.5 4.5 0 0 1 20 10c0 5.8-8 11-8 11z" fill="none" stroke="#e9788f" stroke-width="2"/></svg></div></article>
  <article class="prop"><div class="ph bld" role="img" aria-label="マンション外観の写真"><span class="badge">NEW</span></div><div class="price">7.8万<small>管理費5,000円</small></div><h3>三重中央コロトク・ロフト付き高級物件 パラダン</h3><div class="meta"><span>1K / 24.5㎡ / 駅徒歩5分</span><svg class="heart" viewBox="0 0 24 24"><path d="M12 21s-8-5.2-8-11a4.5 4.5 0 0 1 8-2.8A4.5 4.5 0 0 1 20 10c0 5.8-8 11-8 11z" fill="none" stroke="#e9788f" stroke-width="2"/></svg></div></article>
  <article class="prop"><div class="ph bld" role="img" aria-label="マンション外観の写真"><span class="badge">NEW</span></div><div class="price">7.8万<small>管理費5,000円</small></div><h3>三重中央コロトク・ロフト付き高級物件 パラダン</h3><div class="meta"><span>1K / 24.5㎡ / 駅徒歩5分</span><svg class="heart" viewBox="0 0 24 24"><path d="M12 21s-8-5.2-8-11a4.5 4.5 0 0 1 8-2.8A4.5 4.5 0 0 1 20 10c0 5.8-8 11-8 11z" fill="none" stroke="#e9788f" stroke-width="2"/></svg></div></article>
  <article class="prop"><div class="ph bld" role="img" aria-label="マンション外観の写真"><span class="badge">NEW</span></div><div class="price">7.8万<small>管理費5,000円</small></div><h3>三重中央コロトク・ロフト付き高級物件 パラダン</h3><div class="meta"><span>1K / 24.5㎡ / 駅徒歩5分</span><svg class="heart" viewBox="0 0 24 24"><path d="M12 21s-8-5.2-8-11a4.5 4.5 0 0 1 8-2.8A4.5 4.5 0 0 1 20 10c0 5.8-8 11-8 11z" fill="none" stroke="#e9788f" stroke-width="2"/></svg></div></article>
</section>

<div class="abs hd hd-col"><span class="en">COLUM</span><span class="ja">コラム</span></div>
<div class="abs hd hd-rank"><span class="en">RANKING</span><span class="ja">人気物件ランキング</span></div>

<section class="abs cols">
  <article class="col"><div class="ph food" role="img" aria-label="作り置きおかずの写真"><span class="tag">簡単レシピ</span></div><p>ひとり暮らしの簡単すぎる作り置き<br>7日分材料費900円で料理してみた</p></article>
  <article class="col"><div class="ph person" role="img" aria-label="部屋でくつろぐ女性の写真"><span class="tag">暮らし</span></div><p>ひとり暮らしの簡単すぎる作り置き<br>7日分材料費900円で料理してみた</p></article>
  <article class="col"><div class="ph food" role="img" aria-label="朝ごはんの写真"><span class="tag">簡単レシピ</span></div><p>ひとり暮らしの簡単すぎる作り置き<br>7日分材料費900円で料理してみた</p></article>
  <article class="col"><div class="ph food" role="img" aria-label="食卓の写真"><span class="tag">簡単レシピ</span></div><p>ひとり暮らしの簡単すぎる作り置き<br>7日分材料費900円で料理してみた</p></article>
  <article class="col"><div class="ph person" role="img" aria-label="部屋で過ごす女性の写真"><span class="tag">暮らし</span></div><p>ひとり暮らしの簡単すぎる作り置き<br>7日分材料費900円で料理してみた</p></article>
  <article class="col"><div class="ph room" role="img" aria-label="ベッドのある部屋の写真"><span class="tag">お部屋紹介</span></div><p>ひとり暮らしの簡単すぎる作り置き<br>7日分材料費900円で料理してみた</p></article>
</section>
<ul class="abs pager"><li>&lt;</li><li class="on">1</li><li>2</li><li>3</li><li>4</li><li>&gt;</li></ul>

<ol class="abs rank">
  <li><div class="ph bld" role="img" aria-label="物件外観の写真"></div><div><b>三重中央コロトク・ロフト付き高級物件 パラダン</b><span class="pr">7.8万</span> 1K / 24.5㎡</div></li>
  <li><div class="ph bld" role="img" aria-label="物件外観の写真"></div><div><b>三重中央コロトク・ロフト付き高級物件 パラダン</b><span class="pr">7.8万</span> 1K / 24.5㎡</div></li>
  <li><div class="ph bld" role="img" aria-label="物件外観の写真"></div><div><b>三重中央コロトク・ロフト付き高級物件 パラダン</b><span class="pr">7.8万</span> 1K / 24.5㎡</div></li>
  <li><div class="ph bld" role="img" aria-label="物件外観の写真"></div><div><b>三重中央コロトク・ロフト付き高級物件 パラダン</b><span class="pr">7.8万</span> 1K / 24.5㎡</div></li>
  <li><div class="ph bld" role="img" aria-label="物件外観の写真"></div><div><b>三重中央コロトク・ロフト付き高級物件 パラダン</b><span class="pr">7.8万</span> 1K / 24.5㎡</div></li>
</ol>

<div class="abs hd hd-other"><span class="en">OTHER</span><span class="ja">その他のカテゴリー</span></div>
<ul class="abs other">
  <li>お部屋のこと<span class="ph room" role="img" aria-label="部屋の写真"></span></li>
  <li>暮らしのこと<span class="ph person" role="img" aria-label="暮らしの写真"></span></li>
  <li>街のこと<span class="ph bld" role="img" aria-label="街並みの写真"></span></li>
  <li>レシピのこと<span class="ph food" role="img" aria-label="料理の写真"></span></li>
</ul>

<section class="abs contact">
  <p>物件へのお問い合わせや気になることがございましたら、お気軽にお問い合わせください。</p>
  <div class="row">
    <div class="tel"><svg width="28" height="28" viewBox="0 0 24 24"><path d="M6.6 10.8a15 15 0 0 0 6.6 6.6l2.2-2.2a1 1 0 0 1 1-.25 11.4 11.4 0 0 0 3.6.6 1 1 0 0 1 1 1V20a1 1 0 0 1-1 1A17 17 0 0 1 3 4a1 1 0 0 1 1-1h3.5a1 1 0 0 1 1 1 11.4 11.4 0 0 0 .6 3.6 1 1 0 0 1-.25 1z" fill="#e9788f"/></svg><div>06-4827-3150<small>受付時間 10:00〜18:00（水曜定休）</small></div></div>
    <span class="btn talk">Talkline公式アカウント</span>
    <span class="btn mail">メールフォーム</span>
  </div>
</section>

<footer class="abs footer">
  <div class="abs f-logo"><span class="name">ふわりのおへや</span><span class="mark"></span></div>
  <div class="abs f-co"><b>株式会社 ふわり不動産</b><br>TEL 06-4827-3150<br>大阪府大阪市中央区ふわり町1-2-3</div>
  <ul class="abs f-links"><li>・運営会社</li><li>・プライバシーポリシー</li><li>・お問い合わせ</li></ul>
  <ul class="abs f-sns"><li>・Chirpyアカウント</li><li>・Facelinkアカウント</li><li>・Picroomアカウント</li><li>・Talkline公式アカウント</li></ul>
  <div class="abs copy">©FUWARI INC. ALL RIGHTS RESERVED.</div>
</footer>

</body>
</html>
```